Corvale Spine & Joint Business Card

Need a business card using the logo provided. I want brand side of the card to be grey with the logo in the center of the card in white.

On the other side I leave to the designers

Target Market(s)

Personal Injury Attorneys

Industry/Entity Type

Medical

Contact Information for Business Card

Name, CEO. Cell Phone, (Palmcrest, Address, Phone) (Brookhollow, Address, Phone) (Cedarline, Address, Phone)

Colors

Designer to choose only greyscale colors for use in the design.

Requirements
Must have
• Logo by itself on one side

```html
<!DOCTYPE html>
<html lang="en">
<head>
<meta charset="utf-8">
<title>Corvale Spine &amp; Joint Business Card</title>
<link rel="stylesheet" href="https://fonts.googleapis.com/css2?family=Open+Sans:wght@400;600;700&display=swap">
<style>
  :root {
    --backdrop: #cdc9ca;
    --card: #1a1a1a;
    --accent: #a8a8a8;
    --muted: #8a8a8a;
    --ink: #ffffff;
  }
  * { box-sizing: border-box; margin: 0; padding: 0; }
  html, body {
    width: 1200px; height: 1200px; overflow: hidden;
    background: var(--backdrop);
    font-family: "Open Sans", sans-serif;
  }
  .canvas { position: relative; width: 1200px; height: 1200px; }
  .card {
    position: absolute; left: 229px; width: 744px;
    background: var(--card); color: var(--ink);
  }
  .card--front { top: 163px; height: 420px; }
  .card--back { top: 620px; height: 415px; }

  .brand-mark {
    position: absolute; left: 26px; top: 22px;
    color: var(--ink); font-weight: 600; text-transform: uppercase;
    display: flex; flex-direction: column; align-items: center;
  }
  .brand-mark__name { font-size: 52px; letter-spacing: 0.14em; line-height: 1; padding-left: 0.14em; }
  .brand-mark__sub { font-size: 25px; letter-spacing: 0.22em; line-height: 1; margin-top: 12px; padding-left: 0.22em; }

  .holder {
    position: absolute; right: 28px; top: 176px; text-align: right;
  }
  .holder__name {
    color: var(--accent); font-weight: 700; font-size: 28px; line-height: 1;
  }
  .holder__title { font-size: 17px; margin-top: 10px; line-height: 1; }
  .holder__cell {
    display: flex; justify-content: flex-end; align-items: center; gap: 5px;
    font-size: 17px; margin-top: 10px; line-height: 1;
  }
  .holder__cell svg { width: 14px; height: 18px; }

  .divider {
    position: absolute; left: 26px; right: 27px; top: 292px;
    height: 2px; background: var(--accent);
  }
  .locations {
    position: absolute; left: 26px; right: 27px; top: 308px;
    display: grid; grid-template-columns: repeat(3, 1fr); gap: 20px;
  }
  .location { font-size: 13.5px; line-height: 20px; }
  .location__city {
    color: var(--accent); font-weight: 700; font-size: 14px;
    text-transform: uppercase; letter-spacing: 0.08em;
  }
  .location__phone { display: flex; align-items: center; gap: 5px; }
  .location__phone svg { width: 13px; height: 15px; }

  .brand-lockup {
    position: absolute; inset: 0;
    display: flex; flex-direction: column; align-items: center; justify-content: center;
    color: var(--ink); font-weight: 600; text-transform: uppercase;
  }
  .brand-lockup__name { font-size: 104px; letter-spacing: 0.12em; line-height: 1; padding-left: 0.12em; }
  .brand-lockup__sub { font-size: 54px; letter-spacing: 0.2em; line-height: 1; margin-top: 22px; padding-left: 0.2em; }
</style>
</head>
<body>
<main class="canvas">
  <section class="card card--front">
    <div class="brand-mark">
      <div class="brand-mark__name">Corvale</div>
      <div class="brand-mark__sub">Spine &amp; Joint</div>
    </div>

    <div class="holder">
      <div class="holder__name">DANIEL REYHART</div>
      <div class="holder__title">CEO</div>
      <div class="holder__cell">
        <svg viewBox="0 0 15 19" aria-hidden="true"><rect x="2" y="1" width="11" height="17" rx="2" fill="none" stroke="#a8a8a8" stroke-width="1.6"/><rect x="4" y="3.5" width="7" height="10" fill="#a8a8a8"/><circle cx="7.5" cy="15.8" r="1" fill="#a8a8a8"/></svg>
        <span>+123-456-789</span>
      </div>
    </div>

    <div class="divider"></div>

    <div class="locations">
      <div class="location">
        <div class="location__city">Palmcrest</div>
        <div>4120 Larkmont Avenue #214</div>
        <div>Palmcrest, FL 33012</div>
        <div class="location__phone">
          <svg viewBox="0 0 15 19" aria-hidden="true"><path d="M3 4c1-1 2-1 2.5 0l1.3 2.4c.3.6.1 1.1-.4 1.5l-.8.6c.6 1.6 1.8 3 3.2 3.8l.7-.7c.4-.4 1-.5 1.5-.2l2.3 1.4c.7.5.7 1.3 0 2.1-1 1.2-2.6 1.5-4 .8C5.6 14.4 3.2 11.4 2.3 8 2 6.5 2.2 5 3 4z" fill="#a8a8a8"/></svg>
          <span>+123-456-780</span>
        </div>
      </div>
      <div class="location">
        <div class="location__city">Brookhollow</div>
        <div>2875 Westmere Road #105</div>
        <div>Brookhollow, FL 33030</div>
        <div class="location__phone">
          <svg viewBox="0 0 15 19" aria-hidden="true"><path d="M3 4c1-1 2-1 2.5 0l1.3 2.4c.3.6.1 1.1-.4 1.5l-.8.6c.6 1.6 1.8 3 3.2 3.8l.7-.7c.4-.4 1-.5 1.5-.2l2.3 1.4c.7.5.7 1.3 0 2.1-1 1.2-2.6 1.5-4 .8C5.6 14.4 3.2 11.4 2.3 8 2 6.5 2.2 5 3 4z" fill="#a8a8a8"/></svg>
          <span>+123-456-781</span>
        </div>
      </div>
      <div class="location">
        <div class="location__city">Cedarline</div>
        <div>610 Harwick Parkway #3</div>
        <div>Cedarline, FL 32301</div>
        <div class="location__phone">
          <svg viewBox="0 0 15 19" aria-hidden="true"><path d="M3 4c1-1 2-1 2.5 0l1.3 2.4c.3.6.1 1.1-.4 1.5l-.8.6c.6 1.6 1.8 3 3.2 3.8l.7-.7c.4-.4 1-.5 1.5-.2l2.3 1.4c.7.5.7 1.3 0 2.1-1 1.2-2.6 1.5-4 .8C5.6 14.4 3.2 11.4 2.3 8 2 6.5 2.2 5 3 4z" fill="#a8a8a8"/></svg>
          <span>+123-456-782</span>
        </div>
      </div>
    </div>
  </section>

  <section class="card card--back">
    <div class="brand-lockup">
      <div class="brand-lockup__name">Corvale</div>
      <div class="brand-lockup__sub">Spine &amp; Joint</div>
    </div>
  </section>
</main>
</body>
</html>
```